Logo, letterhead and business card design for fun, different NYC consulting firm

THE BRISTAVEN GROUP - We are looking for an identity package (logo, letterhead, business cards) that makes high-potential entrepreneurs and enterprising corporate executives trip over each other in their race to work with our startup "gurus." We coach and advise individuals (entrepreneurs and corporate executives) and consult organizations (startups and established companies) who want to unlock their entrepreneurial spirit so they can launch new ventures faster, with less investment and greater promise. On the big end, we helped Pelvanix rollout a new line of mobile accessories; on the small side, we helped a Florida woman start an elder care business that now employes 60 people.
Our President is a high-energy, generous guy. He's one of the most fun, approachable, and inspired millionaires I've ever met. His charisma alone makes entrepreneurs and executives of all stripes want to work with him-and these qualities are what we'd like to translate into our logo and other identity pieces.
Please, please, please don't go to the company's website to get a feel for us-the site is horrible, it's not our "vibe," and it's going to be re-imagined, stat!
Instead, know this:
we love startups
we are the home of creative ideas
we support entrepreneurs and enterprising corporate executives in everything they do
we create wealth and value
we help the world
The Bristaven Group is composed of entrepreneur-gurus who are:
fun
independent
born to challenge
unconventional
practical
action-oriented
creative
balanced
Our tagline is:
freeing the founder's bold ambition | growing fresh enterprises
Our business includes:
mentoring | strategy | guidance
We plan on extending the winning identity to our website, so there may be more work in it for you beyond this initial package (more money, yeah!).
Our letterhead will be used almost exclusively as a background in Microsoft Word (we're not sure if we'll get it printed); and the business card should be double-sided, with an optional 2D barcode (if it works well into your design).
Updates
Dear designers -
Target Market(s)
People and organizations who are looking to launch new business ventures more quickly, affordably, and successfully than the competition
Industry/Entity Type
Investment
Requirements
Must have
- Business cards:
- company name: The Bristaven Group
- web address: www.bristavengroup.example
- physical address: 14 Corvath Road, Harlow Point, ME 04011
- name and title: Paul Denholtz, President
- phone number: 203.555.0148
- e-mail address: pdenholtz@bristavengroup.example
- tagline: freeing the founder's bold ambition | growing fresh enterprises
- the card should be double-sided; on the back it should say: mentoring | strategy | guidance (it's up to you if you want to put the company name and logo on the back and/or a QR code)
Letterhead:
- company name: The Bristaven Group (along with mentoring | strategy | guidance somewhere on the page)

```html
<!DOCTYPE html>
<html lang="en">
<head>
<meta charset="utf-8">
<title>The Bristaven Group – Business Card</title>
<link rel="stylesheet" href="https://fonts.googleapis.com/css2?family=Questrial&display=swap">
<style>
  :root {
    --page-bg: #e6e9ec;
    --card-white: #ffffff;
    --card-sky: #6cc6ef;
    --brand-blue: #1565c0;
    --brand-deep: #0d4f9e;
    --brand-mid: #3d8fd8;
    --ink: #1e2a36;
    --ink-soft: #3a4652;
    --tint: #e3f1fb;
  }
  * { box-sizing: border-box; margin: 0; padding: 0; }
  html, body {
    width: 1200px; height: 960px; overflow: hidden;
    background: var(--page-bg);
    font-family: "Questrial", "Helvetica Neue", Arial, sans-serif;
  }
  .sheet {
    width: 1200px; height: 960px;
    display: flex; flex-direction: column; align-items: center; justify-content: center;
    gap: 56px;
  }
  .card {
    position: relative;
    width: 660px; height: 377px;
    overflow: hidden;
    box-shadow: 0 6px 18px rgba(20, 40, 60, 0.18);
  }

  /* ---------- back side ---------- */
  .card--back { background: var(--card-sky); }
  .card--back .brand {
    position: absolute; left: 110px; top: 128px;
    display: flex; align-items: center; gap: 22px;
  }
  .brand-square {
    width: 74px; height: 74px; background: var(--brand-deep);
  }
  .card--back .brand-name {
    font-size: 52px; letter-spacing: 2px; color: var(--brand-deep);
    line-height: 1; font-weight: 400;
  }
  .card--back .brand-rule {
    position: absolute; left: 206px; top: 206px; width: 360px; height: 2px;
    background: var(--brand-blue);
  }
  .card--back .services {
    position: absolute; left: 206px; top: 218px;
    font-size: 25px; color: var(--brand-blue); letter-spacing: 0.5px;
  }

  /* ---------- front side ---------- */
  .card--front { background: var(--card-white); }
  .card--front .accent-panel {
    position: absolute; right: 0; top: 0; width: 210px; height: 300px;
    background: var(--tint);
  }
  .card--front .brand {
    position: absolute; left: 48px; top: 28px;
    display: flex; align-items: center; gap: 16px;
  }
  .card--front .brand-square { width: 40px; height: 40px; background: var(--brand-blue); }
  .card--front .brand-name {
    font-size: 30px; letter-spacing: 2px; color: var(--brand-blue); line-height: 1;
  }
  .person {
    position: absolute; left: 48px; top: 100px; width: 350px;
    font-size: 24px; font-weight: 400; color: var(--ink); letter-spacing: 0.5px;
    padding-bottom: 6px; border-bottom: 2px solid var(--brand-blue);
  }
  .contact {
    position: absolute; left: 58px; top: 150px;
    font-size: 15px; line-height: 22px; color: var(--ink-soft); letter-spacing: 0.4px;
    list-style: none;
  }
  .address {
    position: absolute; left: 48px; top: 222px;
    font-size: 17px; line-height: 22px; color: var(--ink); letter-spacing: 0.4px;
    font-style: normal;
  }
  .address .web { color: var(--brand-blue); display: block; }
  .tagline-band {
    position: absolute; left: 0; right: 0; top: 300px; height: 28px;
    background: var(--brand-mid);
    color: var(--card-white); font-size: 15px; letter-spacing: 0.8px;
    display: flex; align-items: center; justify-content: flex-end; padding-right: 42px;
  }
  .tagline-base {
    position: absolute; left: 0; right: 0; top: 328px; height: 10px;
    background: var(--brand-blue);
  }
</style>
</head>
<body>
<main class="sheet">
  <section class="card card--back" aria-label="Business card, back">
    <div class="brand">
      <span class="brand-square"></span>
      <span class="brand-name">BRISTAVEN</span>
    </div>
    <div class="brand-rule"></div>
    <p class="services">mentoring | strategy | guidance</p>
  </section>

  <section class="card card--front" aria-label="Business card, front">
    <div class="accent-panel"></div>
    <div class="brand">
      <span class="brand-square"></span>
      <span class="brand-name">BRISTAVEN</span>
    </div>
    <h1 class="person">Paul Denholtz, President</h1>
    <ul class="contact">
      <li>t: 203.555.0148</li>
      <li>e: pdenholtz@bristavengroup.example</li>
    </ul>
    <address class="address">
      14 Corvath Road, Harlow Point, ME 04011
      <span class="web">www.bristavengroup.example</span>
    </address>
    <p class="tagline-band">freeing the founder's bold ambition | growing fresh enterprises</p>
    <div class="tagline-base"></div>
  </section>
</main>
</body>
</html>
```